Dean Hollis Business Card

In addition to my name design (file uploaded), black print on white card stock, e-mail address should be presented as a typical e-mail address, i.e., underlined and in blue ink, the card should include the following information:
Professor of Aviation Technology
Accident Litigation Expert Witness
Master Certificated Flight Instructor

dhollis@vexmail.example
Anchorage, Alaska
(907) 318-5074

```html
<!DOCTYPE html>
<html lang="en">
<head>
<meta charset="UTF-8">
<title>Dean Hollis Business Card</title>
<link rel="stylesheet" href="https://fonts.googleapis.com/css2?family=Saira:wght@500;800&family=Source+Sans+3:wght@600&display=swap">
<style>
  :root {
    --page-bg: #e6e4e0;
    --card-bg: #ffffff;
    --ink: #1a1a1a;
    --ink-soft: #2b2b2b;
    --link-blue: #1a1aa6;
    --card-shadow: rgba(0, 0, 0, 0.18);
  }
  html, body {
    margin: 0;
    padding: 0;
    width: 1200px;
    height: 1200px;
    overflow: hidden;
    background: var(--page-bg);
  }
  .canvas {
    position: relative;
    width: 1200px;
    height: 1200px;
  }
  .business-card {
    position: absolute;
    left: 100px;
    top: 315px;
    width: 1000px;
    height: 571px;
    background: var(--card-bg);
    box-shadow: 0 10px 30px var(--card-shadow);
    box-sizing: border-box;
  }
  .credentials {
    position: absolute;
    top: 34px;
    right: 48px;
    margin: 0;
    padding: 0;
    list-style: none;
    text-align: right;
    font-family: "Source Sans 3", sans-serif;
    font-weight: 600;
    font-size: 21px;
    line-height: 24px;
    color: var(--ink-soft);
  }
  .identity {
    position: absolute;
    left: 48px;
    bottom: 52px;
  }
  .holder-name {
    margin: 0;
    font-family: "Saira", sans-serif;
    font-weight: 800;
    font-size: 70px;
    line-height: 1;
    letter-spacing: 2px;
    color: var(--ink);
  }
  .contact-line {
    margin: 6px 0 0 2px;
    font-family: "Saira", sans-serif;
    font-weight: 500;
    font-size: 16px;
    letter-spacing: 2.4px;
    color: var(--ink-soft);
  }
  .contact-line .divider {
    margin: 0 6px;
  }
  .contact-line .email {
    color: var(--link-blue);
    text-decoration: underline;
    font-weight: 800;
  }
</style>
</head>
<body>
  <main class="canvas">
    <section class="business-card">
      <ul class="credentials">
        <li>Professor of Aviation Technology</li>
        <li>Accident Litigation Expert Witness</li>
        <li>Master Certificated Flight Instructor</li>
      </ul>
      <div class="identity">
        <h1 class="holder-name">DEAN E. HOLLIS</h1>
        <p class="contact-line">
          <span class="phone">(907) 318-5074</span><span class="divider">|</span><span class="email">dhollis@vexmail.example</span><span class="divider">|</span><span class="city">Anchorage, Alaska</span>
        </p>
      </div>
    </section>
  </main>
</body>
</html>
```